Bluerock Custom Water Tank

I primarily market the water tanks so want a business care that reflects that. I have attached the water tank logo. You have been working on our water tank so maybe we can use that on the card et. I am leaving as one sided but can be double sided if that works. The information that needs to be on the cards is as follows: Dennis K. Marlow Phone numbers: Office 555-318-4720 Direct 555-260-9134 Mobile 555-482-1657 email address: dennis@fieldgearsupply.example Address P.O. Box 3827 Lakemont, GA 30519 Web Page: www.fieldgearsupply.example. A lot to fit on the card. Thanks

```html
<!DOCTYPE html>
<html lang="en">
<head>
<meta charset="utf-8">
<title>Bluerock – Business Card</title>
<link rel="stylesheet" href="https://fonts.googleapis.com/css2?family=Oswald:wght@500;600&family=Jost:wght@400&family=Roboto:wght@500&display=swap">
<style>
  :root {
    --brand-red: #fb0000;
    --ink: #1c1c1c;
    --text-grey: #555555;
    --card-white: #ffffff;
    --backdrop: #6f6f6f;
  }
  * { box-sizing: border-box; margin: 0; padding: 0; }
  html, body { width: 1200px; height: 1200px; overflow: hidden; }
  body { background: var(--backdrop); position: relative; }

  .card {
    position: absolute;
    left: 262px;
    width: 686px;
    height: 392px;
    overflow: hidden;
  }
  .card--front { top: 165px; background: var(--card-white); }
  .card--back  { top: 653px; background: var(--brand-red); }

  .name-marker {
    position: absolute; left: 0; top: 139px;
    width: 0; height: 0;
    border-top: 19px solid transparent;
    border-bottom: 19px solid transparent;
    border-left: 26px solid var(--brand-red);
  }
  .holder-name {
    position: absolute; left: 48px; top: 140px;
    font-family: "Oswald", sans-serif; font-weight: 500;
    font-size: 28px; line-height: 34px; letter-spacing: 0.2px;
    color: var(--brand-red); text-transform: uppercase;
  }
  .name-rule {
    position: absolute; left: 48px; top: 189px;
    width: 589px; height: 3px; background: var(--ink);
  }

  .brand-lockup {
    position: absolute; right: 49px; top: 118px;
    display: flex; align-items: center; gap: 12px;
  }
  .brand-square { width: 26px; height: 26px; background: var(--brand-red); }
  .brand-name {
    font-family: "Oswald", sans-serif; font-weight: 600;
    font-size: 30px; line-height: 1.05; color: var(--ink);
    text-transform: uppercase; text-align: right;
  }
  .brand-name span { display: block; font-size: 17px; letter-spacing: 0.6px; }

  .contact-list {
    position: absolute; left: 51px; top: 280px; list-style: none;
    font-family: "Jost", sans-serif; font-size: 16px; line-height: 19.5px;
    color: var(--text-grey);
  }
  .contact-list li { display: flex; align-items: center; gap: 6px; }
  .contact-list svg { width: 13px; height: 13px; fill: var(--brand-red); flex: none; }

  .postal {
    position: absolute; right: 49px; top: 300px; text-align: right;
    font-family: "Jost", sans-serif; font-size: 16px; line-height: 19.5px;
    color: var(--text-grey); font-style: normal;
  }
  .postal .web { color: var(--brand-red); }

  .back-lockup {
    position: absolute; left: 0; right: 0; top: 150px;
    display: flex; justify-content: center; align-items: center; gap: 16px;
  }
  .back-square { width: 40px; height: 40px; background: var(--card-white); }
  .back-name {
    font-family: "Oswald", sans-serif; font-weight: 600;
    font-size: 48px; line-height: 1; color: var(--card-white);
    text-transform: uppercase;
  }
  .back-web {
    position: absolute; left: 0; right: 0; top: 338px; text-align: center;
    font-family: "Roboto", sans-serif; font-weight: 500;
    font-size: 15px; letter-spacing: 6.8px; color: var(--card-white);
    text-transform: uppercase;
  }
</style>
</head>
<body>

<section class="card card--front" aria-label="Business card front">
  <div class="name-marker"></div>
  <h1 class="holder-name">Dennis K. Marlow</h1>
  <div class="name-rule"></div>

  <div class="brand-lockup">
    <div class="brand-square"></div>
    <p class="brand-name">Bluerock<span>Storage Systems</span></p>
  </div>

  <ul class="contact-list">
    <li><svg viewBox="0 0 24 24" aria-hidden="true"><path d="M6.6 10.8a15.1 15.1 0 0 0 6.6 6.6l2.2-2.2c.3-.3.7-.4 1-.2 1.1.4 2.3.6 3.6.6.6 0 1 .4 1 1V20c0 .6-.4 1-1 1C10.6 21 3 13.4 3 4c0-.6.4-1 1-1h3.5c.6 0 1 .4 1 1 0 1.3.2 2.5.6 3.6.1.3 0 .7-.2 1z"/></svg>555-318-4720</li>
    <li><svg viewBox="0 0 24 24" aria-hidden="true"><path d="M6.6 10.8a15.1 15.1 0 0 0 6.6 6.6l2.2-2.2c.3-.3.7-.4 1-.2 1.1.4 2.3.6 3.6.6.6 0 1 .4 1 1V20c0 .6-.4 1-1 1C10.6 21 3 13.4 3 4c0-.6.4-1 1-1h3.5c.6 0 1 .4 1 1 0 1.3.2 2.5.6 3.6.1.3 0 .7-.2 1z"/></svg>555-260-9134</li>
    <li><svg viewBox="0 0 24 24" aria-hidden="true"><path d="M7 1h10a2 2 0 0 1 2 2v18a2 2 0 0 1-2 2H7a2 2 0 0 1-2-2V3a2 2 0 0 1 2-2zm0 3v15h10V4z"/></svg>555-482-1657</li>
    <li><svg viewBox="0 0 24 24" aria-hidden="true"><path d="M2 5h20v14H2zm2 2v.5l8 5 8-5V7zm0 3v7h16v-7l-8 5z"/></svg>dennis@fieldgearsupply.example</li>
  </ul>

  <address class="postal">
    P.O. Box 3827<br>
    Lakemont, GA 30519<br>
    <span class="web">www.fieldgearsupply.example</span>
  </address>
</section>

<section class="card card--back" aria-label="Business card back">
  <div class="back-lockup">
    <div class="back-square"></div>
    <p class="back-name">Bluerock</p>
  </div>
  <p class="back-web">www.fieldgearsupply.example</p>
</section>

</body>
</html>
```